We need an attractive business card design that is modern and inviting. We like the blue and yellow (or gold) colors that are displayed with the logo. The business should communicate trust, experience, and integrity.

Target Market(s)

Residential and Commercial

Industry/Entity Type

Business

Contact Information for Business Card

Recessed Lighting
LED Retro Fit
Sign Repair
Alarms and Cameras
Mobile Home Services
24hr service calls

Font styles to use
Serif
Sans Serif

Colors
3176b5
0455a3
fece3e
fbee3e

Requirements
Must have
• Brondle Electric
• Owner: Marcus Tivane
• Licensed and Insured
• TECL #58917
Nice to have
• Exquisite Detail!!
• Over 20 years of experience
Should not have
• Nothing boring or traditional!!!

```html
<!DOCTYPE html>
<html lang="en">
<head>
<meta charset="utf-8">
<title>Brondle Electric business cards</title>
<link rel="stylesheet" href="https://fonts.googleapis.com/css2?family=Lato:wght@400;700&family=Montserrat:wght@700;800&display=swap">
<style>
  :root {
    --blue-light: #3176b5;
    --blue-deep: #0455a3;
    --gold: #fece3e;
    --yellow: #fbee3e;
    --paper: #ffffff;
    --stage: #333436;
  }
  * { box-sizing: border-box; margin: 0; padding: 0; }
  html, body {
    width: 1200px; height: 997px; overflow: hidden;
    background: var(--stage);
  }
  .card {
    position: absolute; left: 280px;
    width: 640px; height: 366px;
    background: var(--paper);
    border-radius: 22px; overflow: hidden;
  }
  .card-back { top: 80px; }
  .card-front { top: 526px; }
  .card-art { position: absolute; inset: 0; width: 100%; height: 100%; }

  .brand {
    position: absolute; right: 44px; top: 44px;
    display: flex; align-items: center; gap: 12px;
  }
  .brand-dot {
    width: 40px; height: 40px; border-radius: 50%;
    border: 4px solid var(--blue-light);
  }
  .brand-name {
    font-family: "Montserrat", sans-serif; font-weight: 800;
    font-size: 26px; letter-spacing: 1px; color: var(--blue-deep);
  }
  .credentials {
    position: absolute; right: 44px; top: 94px;
    font-family: "Lato", sans-serif; font-weight: 700;
    font-size: 13px; letter-spacing: 1px; color: var(--blue-light);
  }

  .services {
    position: absolute; left: 44px; top: 118px;
    list-style: none;
    font-family: "Lato", sans-serif; font-size: 19px;
    color: var(--blue-light);
  }
  .services li { display: flex; align-items: center; gap: 10px; height: 30px; }
  .tick { width: 16px; height: 16px; flex: none; }

  .website {
    position: absolute; right: 30px; bottom: 26px;
    font-family: "Lato", sans-serif; font-size: 14px; letter-spacing: 1.5px;
    color: var(--paper);
  }

  .owner { position: absolute; left: 42px; top: 116px; }
  .owner-name {
    font-family: "Montserrat", sans-serif; font-weight: 700;
    font-size: 27px; line-height: 1.2; color: var(--blue-deep);
  }
  .owner-role {
    font-family: "Montserrat", sans-serif; font-weight: 700;
    font-size: 13px; color: var(--blue-deep); margin-top: 2px; margin-left: 6px;
  }

  .contacts {
    position: absolute; left: 34px; top: 268px;
    list-style: none;
    font-family: "Lato", sans-serif; font-size: 16px; color: var(--paper);
  }
  .contacts li { display: flex; align-items: center; gap: 12px; height: 22px; }
  .contact-icon { width: 16px; height: 16px; flex: none; }
</style>
</head>
<body>

<section class="card card-back" aria-label="Card back: services">
  <svg class="card-art" viewBox="0 0 640 366" aria-hidden="true">
    <path d="M290 366 Q450 225 640 150 L640 176 Q470 240 318 366 Z" fill="var(--yellow)"/>
    <path d="M330 366 Q480 250 640 192 L640 366 Z" fill="var(--blue-deep)"/>
  </svg>
  <div class="brand">
    <span class="brand-dot"></span>
    <span class="brand-name">BRONDLE ELECTRIC</span>
  </div>
  <ul class="services">
    <li><svg class="tick" viewBox="0 0 16 16"><rect x="1" y="1" width="14" height="14" fill="none" stroke="var(--blue-light)" stroke-width="1.6"/><path d="M3.5 8 L7 11.5 L13 3.5" fill="none" stroke="var(--gold)" stroke-width="2.2"/></svg>Sign Repair</li>
    <li><svg class="tick" viewBox="0 0 16 16"><rect x="1" y="1" width="14" height="14" fill="none" stroke="var(--blue-light)" stroke-width="1.6"/><path d="M3.5 8 L7 11.5 L13 3.5" fill="none" stroke="var(--gold)" stroke-width="2.2"/></svg>LED Retro Fit</li>
    <li><svg class="tick" viewBox="0 0 16 16"><rect x="1" y="1" width="14" height="14" fill="none" stroke="var(--blue-light)" stroke-width="1.6"/><path d="M3.5 8 L7 11.5 L13 3.5" fill="none" stroke="var(--gold)" stroke-width="2.2"/></svg>24hr service calls</li>
    <li><svg class="tick" viewBox="0 0 16 16"><rect x="1" y="1" width="14" height="14" fill="none" stroke="var(--blue-light)" stroke-width="1.6"/><path d="M3.5 8 L7 11.5 L13 3.5" fill="none" stroke="var(--gold)" stroke-width="2.2"/></svg>Recessed Lighting</li>
    <li><svg class="tick" viewBox="0 0 16 16"><rect x="1" y="1" width="14" height="14" fill="none" stroke="var(--blue-light)" stroke-width="1.6"/><path d="M3.5 8 L7 11.5 L13 3.5" fill="none" stroke="var(--gold)" stroke-width="2.2"/></svg>Alarms and Cameras</li>
    <li><svg class="tick" viewBox="0 0 16 16"><rect x="1" y="1" width="14" height="14" fill="none" stroke="var(--blue-light)" stroke-width="1.6"/><path d="M3.5 8 L7 11.5 L13 3.5" fill="none" stroke="var(--gold)" stroke-width="2.2"/></svg>Mobile Home Services</li>
    <li><svg class="tick" viewBox="0 0 16 16"><rect x="1" y="1" width="14" height="14" fill="none" stroke="var(--blue-light)" stroke-width="1.6"/><path d="M3.5 8 L7 11.5 L13 3.5" fill="none" stroke="var(--gold)" stroke-width="2.2"/></svg>Residential and Commercial</li>
  </ul>
  <p class="website">www.brondleelectric.com</p>
</section>

<section class="card card-front" aria-label="Card front: owner and contact">
  <svg class="card-art" viewBox="0 0 640 366" aria-hidden="true">
    <path d="M0 246 Q420 150 640 150 L640 160 Q420 162 0 266 Z" fill="var(--yellow)"/>
    <path d="M0 274 Q420 170 640 168 L640 366 L0 366 Z" fill="var(--blue-deep)"/>
  </svg>
  <div class="brand">
    <span class="brand-dot"></span>
    <span class="brand-name">BRONDLE ELECTRIC</span>
  </div>
  <p class="credentials">LICENSED AND INSURED · TECL #58917</p>
  <div class="owner">
    <p class="owner-name">Marcus Tivane</p>
    <p class="owner-role">OWNER</p>
  </div>
  <ul class="contacts">
    <li><svg class="contact-icon" viewBox="0 0 16 16"><path d="M2 6 Q8 1 14 6 L12 8 L10 6.5 L6 6.5 L4 8 Z M4 9 H12 L13 14 H3 Z" fill="var(--gold)"/></svg>303-555-0147</li>
    <li><svg class="contact-icon" viewBox="0 0 16 16"><rect x="4" y="1.5" width="8" height="13" rx="1.5" fill="none" stroke="var(--gold)" stroke-width="1.8"/></svg>060-555-2719</li>
    <li><svg class="contact-icon" viewBox="0 0 16 16"><rect x="1" y="3.5" width="14" height="9" fill="var(--gold)"/><path d="M1 3.5 L8 9 L15 3.5" fill="none" stroke="var(--blue-deep)" stroke-width="1.2"/></svg>hello@brondleelectric.com</li>
    <li><svg class="contact-icon" viewBox="0 0 16 16"><path d="M8 15 Q2 8 3 5.5 A5 5 0 0 1 13 5.5 Q14 8 8 15 Z" fill="var(--gold)"/><circle cx="8" cy="6" r="2" fill="var(--blue-deep)"/></svg>Harlow Creek Station Road 27b</li>
  </ul>
</section>

</body>
</html>
```